Heron Freightlines needs Bussiness cards!

Our new trucking company needs business cards!
We need the same design with two different names and emails, everything else it's the same.
I have included our original logo so we can use it for the design.
Note: the logo to be used is the o e with the buffalo on the right side, next to the letters H and F.

Target Market(s)

Trucking, refrigerated transportation, freight

Industry/Entity Type

Business

Contact Information for Business Card

Card #1:
Marcus Tellwright
marcustellwright@heronfreightlines.example
1-844-555-0193
(555)555-0178
3817 W. Tarrow Ave.
Larkmoor, NM 78599
www.heronfreightlines.example

Card#2:
Orla Brennick
orla@heronfreightlines.example
1-844-555-0193
(555)555-0178
3817 W. Tarrow Ave.
Larkmoor, NM 78599
www.heronfreightlines.example

Font styles to use
Sans Serif

Colors
0655a3
ec1f27
ffffff

Requirements
Must have
• our logo
Nice to have
• roads on background,

```html
<!DOCTYPE html>
<html lang="en">
<head>
<meta charset="utf-8">
<title>Heron Freightlines – Business Cards</title>
<link rel="stylesheet" href="https://fonts.googleapis.com/css2?family=PT+Sans:wght@400;700&display=swap">
<style>
  :root {
    --brand-blue: #0655a3;
    --brand-red: #ec1f27;
    --paper: #ffffff;
    --ink: #3d3d3d;
    --stage: #3b3b3b;
    --fog-top: #f7f7f6;
    --fog-mid: #d9d8d2;
    --road: #7d7773;
  }
  html, body {
    margin: 0;
    padding: 0;
    width: 1200px;
    height: 1200px;
    overflow: hidden;
    background: var(--stage);
    font-family: "PT Sans", sans-serif;
  }
  .canvas {
    position: relative;
    width: 1200px;
    height: 1200px;
  }
  .card {
    position: absolute;
    left: 297px;
    width: 607px;
    height: 344px;
    background: var(--paper);
    overflow: hidden;
  }
  .card--front { top: 214px; }
  .card--back { top: 628px; }

  .road-photo {
    position: absolute;
    inset: 0;
    background: linear-gradient(180deg, var(--fog-top) 0%, #eeede9 30%, var(--fog-mid) 62%, var(--road) 100%);
  }
  .wordmark {
    position: absolute;
    display: flex;
    align-items: center;
    gap: 12px;
    font-weight: 700;
    color: var(--brand-blue);
    white-space: nowrap;
    line-height: 1;
  }
  .wordmark__dot {
    width: 30px;
    height: 30px;
    border-radius: 50%;
    background: var(--brand-red);
    flex: none;
  }
  .card--front .wordmark {
    left: 114px;
    top: 150px;
    font-size: 40px;
  }
  .card--back .wordmark {
    left: 28px;
    top: 66px;
    font-size: 44px;
  }

  .holder {
    position: absolute;
    left: 0;
    top: 198px;
    height: 34px;
    display: flex;
    align-items: center;
  }
  .holder__bar {
    width: 12px;
    height: 34px;
    background: var(--brand-red);
  }
  .holder__name {
    margin-left: 16px;
    font-size: 27px;
    color: var(--brand-blue);
    font-weight: 400;
  }

  .contact-list {
    position: absolute;
    left: 29px;
    top: 248px;
    margin: 0;
    padding: 0;
    list-style: none;
    font-size: 15.5px;
    color: var(--ink);
  }
  .contact-list li {
    display: flex;
    align-items: center;
    height: 21px;
  }
  .contact-list svg {
    width: 12px;
    height: 12px;
    margin-right: 9px;
    flex: none;
  }

  .address {
    position: absolute;
    right: 26px;
    top: 248px;
    text-align: right;
    font-size: 15.5px;
    color: var(--ink);
    line-height: 21px;
    font-style: normal;
  }

  .footer-band {
    position: absolute;
    left: 0;
    bottom: 0;
    width: 607px;
    height: 344px;
    pointer-events: none;
  }
  .website {
    position: absolute;
    right: 24px;
    bottom: 10px;
    font-size: 15px;
    color: var(--paper);
  }
</style>
</head>
<body>
<main class="canvas">

  <section class="card card--front" aria-label="Card front">
    <div class="road-photo" role="img" aria-label="Photo of a winding road through misty autumn woods"></div>
    <div class="wordmark">
      <span class="wordmark__dot"></span>
      <span class="wordmark__name">Heron Freightlines</span>
    </div>
  </section>

  <section class="card card--back" aria-label="Card back">
    <div class="wordmark">
      <span class="wordmark__dot"></span>
      <span class="wordmark__name">Heron Freightlines</span>
    </div>

    <div class="holder">
      <span class="holder__bar"></span>
      <span class="holder__name">Marcus Tellwright</span>
    </div>

    <ul class="contact-list">
      <li>
        <svg viewBox="0 0 12 12" aria-hidden="true"><rect x="0.5" y="2" width="11" height="8" fill="var(--brand-red)"/><path d="M0.5 2.5 L6 6.8 L11.5 2.5" fill="none" stroke="#fff" stroke-width="1.2"/></svg>
        marcustellwright@heronfreightlines.example
      </li>
      <li>
        <svg viewBox="0 0 12 12" aria-hidden="true"><path d="M0.5 4 Q6 0 11.5 4 L10 5.5 L8.5 4.5 L3.5 4.5 L2 5.5 Z" fill="var(--brand-red)"/><rect x="2.5" y="6" width="7" height="5" rx="1" fill="var(--brand-red)"/><circle cx="6" cy="8.5" r="1.2" fill="#fff"/></svg>
        1-844-555-0193
      </li>
      <li>
        <svg viewBox="0 0 12 12" aria-hidden="true"><rect x="2.5" y="0.5" width="7" height="11" rx="1.2" fill="none" stroke="var(--brand-red)" stroke-width="1.4"/><rect x="5" y="9" width="2" height="1" fill="var(--brand-red)"/></svg>
        (555)555-0178
      </li>
    </ul>

    <address class="address">
      3817 W. Tarrow Ave.<br>
      Larkmoor, NM 78599
    </address>

    <svg class="footer-band" viewBox="0 0 607 344" aria-hidden="true">
      <path d="M252 344 C296 318 348 304 410 298 C362 308 320 324 292 344 Z" fill="var(--brand-blue)"/>
      <path d="M282 344 C360 308 470 296 607 294 L607 344 Z" fill="var(--brand-red)"/>
    </svg>
    <span class="website">www.heronfreightlines.example</span>
  </section>

</main>
</body>
</html>
```